Bluerock Data Partners - IT Support Tri-Fold

Need a tri-fold brochure for marketing, pitching managed IT Services. These services include computer/server management, security, cloud backups. The tri-fold should use our logo and colors (Attached)

```html
<!DOCTYPE html>
<html lang="en">
<head>
<meta charset="UTF-8">
<title>Bluerock Data Partners – IT Support Tri-Fold</title>
<link rel="stylesheet" href="https://fonts.googleapis.com/css2?family=Open+Sans:wght@600;700&display=swap">
<style>
  :root {
    --navy: #1e3461;
    --royal: #34519f;
    --edge: #2b2d7a;
    --accent-line: #1b6dc1;
    --red: #e4172b;
    --green: #47ad4f;
    --white: #ffffff;
    --ink: #111111;
    --security-blue: #2d4a9a;
  }
  * { box-sizing: border-box; margin: 0; padding: 0; }
  html, body { width: 1200px; height: 840px; overflow: hidden; background: var(--white); }
  body { font-family: "Open Sans", Arial, sans-serif; }

  .brochure { display: flex; width: 1200px; height: 840px; }
  .panel { position: relative; width: 400px; height: 840px; background: var(--white); }

  .panel__edge { height: 8px; background: var(--edge); }
  .panel--cloud .panel__edge { background: var(--white); }

  .panel__icon-area {
    height: 200px; display: flex; align-items: center; justify-content: center;
    background: var(--royal);
  }
  .panel--cloud .panel__icon-area { background: var(--navy); }
  .panel__icon-area svg { width: 130px; height: 100px; }

  .panel__title {
    position: relative; height: 44px; display: flex; align-items: center; justify-content: center;
    font-size: 25px; font-weight: 700; color: var(--white); z-index: 2;
  }
  .panel__title::after {
    content: ""; position: absolute; left: 50%; top: 44px; transform: translateX(-50%);
    border-left: 16px solid transparent; border-right: 16px solid transparent;
    border-top: 16px solid var(--band);
  }
  .panel--managing .panel__title { background: var(--red); --band: var(--red); }
  .panel--cloud .panel__title { background: var(--green); --band: var(--green); }
  .panel--security .panel__title { background: var(--white); --band: var(--white); color: var(--security-blue); }

  .panel__photo { height: 285px; }
  .panel--managing .panel__photo { background: linear-gradient(135deg, #cfd6dc 0%, #e9e4dc 45%, #c89a6e 100%); }
  .panel--cloud .panel__photo { background: radial-gradient(circle at 50% 45%, #4f86c9 0%, #1d3d78 45%, #0b1a3a 100%); }
  .panel--security .panel__photo { background: radial-gradient(circle at 60% 35%, #e6ebf0 0%, #b9c3cc 60%, #9aa6b2 100%); }

  .panel__rule { height: 6px; background: var(--accent-line); }
  .panel--cloud .panel__rule { background: var(--white); }

  .panel__services-heading {
    height: 48px; display: flex; align-items: center; justify-content: center;
    background: var(--navy); color: var(--white); font-size: 27px; font-weight: 700;
  }

  .service-list {
    list-style: none; height: 239px; padding: 32px 0 0 37px; background: var(--white);
  }
  .panel--cloud .service-list { background: var(--royal); padding-left: 33px; }
  .service-list li {
    display: flex; align-items: center; height: 36px;
    font-size: 17px; font-weight: 600; color: var(--ink);
  }
  .panel--cloud .service-list li { color: var(--white); }
  .service-list svg { width: 22px; height: 22px; margin-right: 14px; flex: none; }

  .panel__footer { height: 10px; background: var(--edge); }
  .panel--cloud .panel__footer { background: var(--white); }
</style>
</head>
<body>
<svg width="0" height="0" style="position:absolute">
  <defs>
    <symbol id="tick-box" viewBox="0 0 22 22">
      <rect x="1.5" y="4.5" width="15" height="15" rx="2" fill="none" stroke="#2d4a9a" stroke-width="2"/>
      <path d="M4.5 11.5 L9 16 L20 3" fill="none" stroke="#e4172b" stroke-width="3" stroke-linecap="round" stroke-linejoin="round"/>
    </symbol>
    <symbol id="tick-box-light" viewBox="0 0 22 22">
      <rect x="1.5" y="4.5" width="15" height="15" rx="2" fill="none" stroke="#ffffff" stroke-width="2"/>
      <path d="M4.5 11.5 L9 16 L20 3" fill="none" stroke="#ffffff" stroke-width="3" stroke-linecap="round" stroke-linejoin="round"/>
    </symbol>
  </defs>
</svg>

<main class="brochure">
  <!-- Managing IT -->
  <section class="panel panel--managing">
    <div class="panel__edge"></div>
    <div class="panel__icon-area">
      <svg viewBox="0 0 130 100" aria-hidden="true">
        <g fill="#fff">
          <rect x="0" y="10" width="70" height="18" rx="3"/>
          <rect x="0" y="32" width="70" height="18" rx="3"/>
          <rect x="0" y="54" width="70" height="18" rx="3"/>
        </g>
        <g fill="#34519f">
          <circle cx="8" cy="19" r="3"/><circle cx="8" cy="41" r="3"/><circle cx="8" cy="63" r="3"/>
        </g>
        <rect x="48" y="34" width="80" height="52" rx="3" fill="#34519f" stroke="#fff" stroke-width="6"/>
        <rect x="78" y="86" width="20" height="8" fill="#fff"/>
        <rect x="68" y="93" width="40" height="5" rx="2" fill="#fff"/>
        <path d="M112 28 Q112 10 94 10" fill="none" stroke="#fff" stroke-width="5"/>
        <path d="M84 10 L96 0 L96 20 Z" fill="#fff"/>
      </svg>
    </div>
    <h2 class="panel__title">Managing IT</h2>
    <div class="panel__photo" role="img" aria-label="Photo of colleagues working together at laptops in a bright office"></div>
    <div class="panel__rule"></div>
    <h3 class="panel__services-heading">Services</h3>
    <ul class="service-list">
      <li><svg><use href="#tick-box"/></svg>Lorem ipsum dolor sit amet.</li>
      <li><svg><use href="#tick-box"/></svg>Lorem ipsum dolor sit.</li>
      <li><svg><use href="#tick-box"/></svg>Lorem ipsum dolor sit amet.</li>
      <li><svg><use href="#tick-box"/></svg>Lorem ipsum dolor sit.</li>
      <li><svg><use href="#tick-box"/></svg>Lorem ipsum dolor sit amet.</li>
    </ul>
    <div class="panel__footer"></div>
  </section>

  <!-- Cloud -->
  <section class="panel panel--cloud">
    <div class="panel__edge"></div>
    <div class="panel__icon-area">
      <svg viewBox="0 0 130 100" aria-hidden="true">
        <path d="M30 62 C14 62 10 42 24 36 C22 20 40 12 50 20 C56 4 84 4 90 22 C104 18 116 30 110 44 C122 50 118 64 104 62"
              fill="none" stroke="#fff" stroke-width="7" stroke-linejoin="round"/>
        <g fill="#fff">
          <rect x="36" y="40" width="60" height="16" rx="3"/>
          <rect x="36" y="60" width="60" height="16" rx="3"/>
          <rect x="36" y="80" width="60" height="16" rx="3"/>
        </g>
        <g fill="#1e3461">
          <rect x="68" y="46" width="20" height="4"/><rect x="68" y="66" width="20" height="4"/><rect x="68" y="86" width="20" height="4"/>
        </g>
      </svg>
    </div>
    <h2 class="panel__title">Cloud</h2>
    <div class="panel__photo" role="img" aria-label="Illustration of a glowing cloud with upload and download arrows above a tablet held in two hands"></div>
    <div class="panel__rule"></div>
    <h3 class="panel__services-heading">Services</h3>
    <ul class="service-list">
      <li><svg><use href="#tick-box-light"/></svg>Lorem ipsum dolor sit amet.</li>
      <li><svg><use href="#tick-box-light"/></svg>Lorem ipsum dolor sit.</li>
      <li><svg><use href="#tick-box-light"/></svg>Lorem ipsum dolor sit amet.</li>
      <li><svg><use href="#tick-box-light"/></svg>Lorem ipsum dolor sit.</li>
      <li><svg><use href="#tick-box-light"/></svg>Lorem ipsum dolor sit amet.</li>
    </ul>
    <div class="panel__footer"></div>
  </section>

  <!-- Security -->
  <section class="panel panel--security">
    <div class="panel__edge"></div>
    <div class="panel__icon-area">
      <svg viewBox="0 0 130 100" aria-hidden="true">
        <g fill="#fff">
          <rect x="10" y="8" width="80" height="22" rx="3"/>
          <rect x="10" y="34" width="80" height="22" rx="3"/>
          <rect x="10" y="60" width="80" height="22" rx="3"/>
        </g>
        <g fill="#34519f">
          <rect x="18" y="17" width="18" height="4"/><rect x="18" y="43" width="18" height="4"/><rect x="18" y="69" width="18" height="4"/>
        </g>
        <path d="M94 20 Q108 30 124 28 L124 56 Q124 80 94 96 Q64 80 64 56 L64 28 Q80 30 94 20 Z" fill="#34519f"/>
        <path d="M94 26 Q106 34 120 33 L120 56 Q120 76 94 90 Q68 76 68 56 L68 33 Q82 34 94 26 Z" fill="#fff"/>
      </svg>
    </div>
    <h2 class="panel__title">Security</h2>
    <div class="panel__photo" role="img" aria-label="Photo of a finger touching a padlock icon on a hexagon grid of cyber security terms"></div>
    <div class="panel__rule"></div>
    <h3 class="panel__services-heading">Services</h3>
    <ul class="service-list">
      <li><svg><use href="#tick-box"/></svg>Lorem ipsum dolor sit amet.</li>
      <li><svg><use href="#tick-box"/></svg>Lorem ipsum dolor sit.</li>
      <li><svg><use href="#tick-box"/></svg>Lorem ipsum dolor sit amet.</li>
      <li><svg><use href="#tick-box"/></svg>Lorem ipsum dolor sit.</li>
      <li><svg><use href="#tick-box"/></svg>Lorem ipsum dolor sit amet.</li>
    </ul>
    <div class="panel__footer"></div>
  </section>
</main>
</body>
</html>
```